Tallow Crest Business Card

We need a business card designed for a a company called "Tallow Crest". We offer consulting, coaching and training to business leaders and coaches (across the world) using the latest findings in neuroscience, social and emotional intelligence and positive psychology. The final design should communicate the use of brain science to create sustainable relationships.

The card should be doublesided. The logo is attached and names and titles will be provided to the successful designer. Thank you.

Industry/Entity Type

Training

```html
<!DOCTYPE html>
<html lang="en">
<head>
<meta charset="utf-8">
<title>Tallow Crest Business Card</title>
<link href="https://fonts.googleapis.com/css2?family=Ubuntu:wght@400;500;700&display=swap" rel="stylesheet">
<style>
  :root {
    --stage: #d9d9d9;
    --card-dark: #2b2d30;
    --card-light: #ffffff;
    --brand-blue: #1b8fd0;
    --brand-lime: #c5d92d;
    --ink: #2e2e2e;
    --ink-soft: #555555;
  }
  * { margin: 0; padding: 0; box-sizing: border-box; }
  html, body { width: 1200px; height: 861px; overflow: hidden; }
  body {
    background: var(--stage);
    font-family: "Ubuntu", sans-serif;
    position: relative;
  }
  .card {
    position: absolute;
    top: 285px;
    width: 480px;
    height: 300px;
    border-radius: 16px;
  }
  .card--front { left: 95px; background: var(--card-dark); }
  .card--back { left: 625px; background: var(--card-light); }
  .card__notch {
    position: absolute;
    top: 90px;
    width: 30px;
    height: 120px;
    background: var(--stage);
    border-radius: 10px;
  }
  .card__notch--left { left: -2px; border-radius: 0 10px 10px 0; }
  .card__notch--right { right: -2px; border-radius: 10px 0 0 10px; }

  .wordmark {
    display: flex;
    align-items: center;
    justify-content: center;
    gap: 12px;
    color: var(--brand-blue);
    font-weight: 700;
  }
  .wordmark__square { background: var(--brand-lime); }
  .card--front .wordmark {
    position: absolute; inset: 0;
    font-size: 44px;
  }
  .card--front .wordmark__square { width: 28px; height: 28px; }

  .card--back .wordmark {
    margin-top: 46px;
    font-size: 26px;
    gap: 8px;
  }
  .card--back .wordmark__square { width: 16px; height: 16px; }

  .holder { text-align: center; margin-top: 22px; }
  .holder__name { font-size: 22px; font-weight: 700; color: var(--ink); }
  .holder__position { font-size: 13px; color: var(--ink-soft); margin-top: 2px; }

  .address {
    display: flex; align-items: center; justify-content: center; gap: 6px;
    font-size: 10px; font-weight: 500; color: var(--ink-soft);
    margin-top: 18px;
  }
  .contacts {
    display: grid;
    grid-template-columns: 120px 120px;
    column-gap: 20px;
    margin: 24px 0 0 160px;
    font-size: 8.5px; font-weight: 500; color: var(--ink-soft);
  }
  .contacts ul { list-style: none; }
  .contacts li { display: flex; align-items: center; gap: 5px; height: 12px; }
  .icon { width: 8px; height: 8px; flex: none; }
  .icon--dot { border-radius: 50%; background: var(--brand-lime); }
</style>
</head>
<body>
  <section class="card card--front" aria-label="Card front">
    <span class="card__notch card__notch--left"></span>
    <span class="card__notch card__notch--right"></span>
    <div class="wordmark"><span class="wordmark__square"></span>Tallow Crest</div>
  </section>

  <section class="card card--back" aria-label="Card back">
    <span class="card__notch card__notch--left"></span>
    <span class="card__notch card__notch--right"></span>
    <div class="wordmark"><span class="wordmark__square"></span>Tallow Crest</div>
    <div class="holder">
      <p class="holder__name">Name Surname</p>
      <p class="holder__position">Position</p>
    </div>
    <p class="address">
      <svg class="icon" viewBox="0 0 10 10"><path d="M5 0.5 0 5h1.5v4.5h2.5V6.5h2v3h2.5V5H10z" fill="var(--brand-blue)"/></svg>
      #48 Sample Avenue, Norfield City. PA 00000
    </p>
    <div class="contacts">
      <ul>
        <li><svg class="icon" viewBox="0 0 10 10"><path d="M2 0.5 4 2.5 3 4c.8 1.4 1.6 2.2 3 3l1.5-1 2 2-1.5 1.5C4.5 9 1 5.5.5 2z" fill="var(--brand-lime)"/></svg>555.014.2288</li>
        <li><svg class="icon" viewBox="0 0 10 10"><rect x="2.5" y="0.5" width="5" height="9" rx="1" fill="var(--brand-lime)"/><rect x="3.5" y="1.8" width="3" height="5" fill="#fff"/></svg>555.019.4471</li>
        <li><svg class="icon" viewBox="0 0 10 10"><rect x="0.5" y="2" width="9" height="6" rx="1" fill="var(--brand-lime)"/><path d="M1 2.5 5 5.5 9 2.5" stroke="#fff" stroke-width="0.8" fill="none"/></svg>name@tallowcrest.com</li>
      </ul>
      <ul>
        <li><span class="icon icon--dot"></span>tallowcrest</li>
        <li><span class="icon icon--dot"></span>tallowcrest</li>
        <li><svg class="icon" viewBox="0 0 10 10"><rect x="0.5" y="1" width="9" height="6" rx="0.8" fill="var(--brand-lime)"/><rect x="3.5" y="7.5" width="3" height="1.5" fill="var(--brand-lime)"/></svg>www.tallowcrest.com</li>
      </ul>
    </div>
  </section>
</body>
</html>
```